Progressive business consultancy seeking innovative and clever powerpoint design

Were looking for a PowerPoint design for our Melbourne based business consulting company, Vantora.

About Us:
Based in Melbourne, Australia, Vantora is a management consulting organisation that partners with their clients to lead the execution of strategic process and system improvement initiatives.

Vantora offers business advisory services in Project Management, Business Process Management, Change Management, Business Analysis and Business Intelligence. Vantora combines hands on delivery with coaching in best practice methodologies and approaches to build our clients capabilities ensuring their ongoing success in project implementations.

Vantora has extensive experience across a wide range of industries. We specialise in assisting organisations across the accounting, legal, financial services and health sectors.

Our core purpose is to help businesses in the middle market navigate transformational change through clear and focused execution and enablement.

www.vantora.com.au
@vantora_hq

What we're looking for:
A PowerPoint template consisting of:
- a front/cover page with hero image (attached)
- a contents page
- a divider page (for different segments of the slide deck)
- a standard PowerPoint content page
- a blank PowerPoint page. (still Vantora themed)

The Vantora colours are white and blue (RGB:0/86/162 and
CMYK 97/73/4/0)

All slides should have the Vantora logo (attached) and a professional, almost corporate, (but not boring) theme that is consistent across all slides. The design should reflect our focus on the "e" in vantora, which is what we're really about - "e"xecution and "e"nablement of change.

I've attached a PNG file of our word template which shows the focus on the "e" as a watermark on the document as well as the font files if required.

Let me know if you need any further information or design specifics.

Thanks,

Marjorie
(on behalf of Desmond)
Updates

Project Deadline Extended
Reason: Hi Designers, We have received some really great designs. Thanks for taking the time to make your submissions. We have decided to extend the deadline as we need some more time to review and consult other colleagues on the great submissions we have received. We are also hoping we might get some additional submissions over the weekend. We would also like enough time to provide feedback on all the submissions received. Thanks for helping us out with some really creative work. Desmond @vantora_hq

Project Deadline Extended
Reason: Hi designers, thanks for taking the time to submit your designs. We have some really great submissions. We are going to have to extend our deadline again as we just haven't had the chance to review and provide feedback on all the designs. We will be closing this project off on Tuesday March 17. Thanks Desmond @vantora_hq

Target Market(s)

C-Level executives (CEO,COO,CIO) at professional services firms (Accounting and Legal), not for profit organisations and financial services firms.

Industry/Entity Type

Management Consulting

Font styles to use
Serif
Other font styles liked:
• Calibri or attached fonts

Requirements
Must have
• A PowerPoint template consisting of:
• 1) a front/cover page with hero image (attached)
• 2) a contents page
• 3) a divider page (for different segments of the slide deck)
• 4) a standard PowerPoint content page
• 5) a blank PowerPoint page. (still Vantora themed)
• 6) Two content
• 7) Comparison
• 8) Table
• 9) Picture column
• 10) Chevron
• The Vantora colours are white and blue (RGB:0/86/162 and
• CMYK 97/73/4/0)

```html
<!DOCTYPE html>
<html lang="en">
<head>
<meta charset="utf-8">
<title>Vantora — Presentation Template</title>
<link href="https://fonts.googleapis.com/css2?family=Montserrat:wght@500;600;700&family=Didact+Gothic&display=swap" rel="stylesheet">
<style>
:root{
  --brand:#0056a2;
  --brand-deep:#003d80;
  --stage:#0a3fa3;
  --ink:#6f7780;
  --rule:#d9dde3;
  --pale:#dbe8f6;
  --paper:#ffffff;
}
*{box-sizing:border-box;margin:0;padding:0}
html,body{width:1200px;height:1200px;overflow:hidden;background:var(--stage)}
body{position:relative;font-family:"Didact Gothic",sans-serif;color:var(--ink)}
.heading{font-family:"Montserrat",sans-serif}

.slide{position:absolute;background:var(--paper);overflow:hidden}
.slide--large{width:467px;height:350px;top:44px}
.slide--thumb{width:252px;height:189px}

.label{position:absolute;font-family:"Montserrat",sans-serif;font-weight:600;color:#fff;font-size:16px;letter-spacing:.3px}
.label--vertical{transform:rotate(-90deg);transform-origin:center;white-space:nowrap;font-size:15px}
.label--thumb{width:252px;text-align:center}

/* common slide parts */
.s-title{position:absolute;left:0;right:0;top:11px;text-align:center;font-family:"Montserrat",sans-serif;font-weight:600;color:var(--brand);font-size:7.4px;letter-spacing:.2px}
.s-num{position:absolute;right:6px;top:4px;width:10px;height:10px;border-radius:50%;background:var(--brand);color:#fff;font-size:3.6px;line-height:10px;text-align:center;font-family:"Montserrat",sans-serif;box-shadow:0 0 0 1px #c6d6ea}
.s-foot{position:absolute;left:9px;right:9px;bottom:5px;display:flex;justify-content:space-between;align-items:center;border-top:.5px solid var(--rule);padding-top:3px}
.brand-mark{font-family:"Montserrat",sans-serif;font-weight:600;color:var(--brand);font-size:5.4px}
.copy{font-size:3px;color:#9aa1a9}
.tiny{font-size:3.2px;line-height:4.4px;color:#8a929b}
.tiny--lead{color:var(--brand);font-weight:bold}
.photo{position:absolute}

/* large inner slide */
.who .title{position:absolute;top:18px;left:0;right:0;text-align:center;font-family:"Montserrat",sans-serif;font-weight:600;color:var(--brand);font-size:15px}
.who .badge{position:absolute;right:16px;top:8px;width:20px;height:20px;border-radius:50%;background:var(--brand);color:#fff;font-size:6.5px;line-height:20px;text-align:center;font-family:"Montserrat",sans-serif;box-shadow:0 0 0 2px #c6d6ea}
.who .portrait{position:absolute;left:16px;top:84px;width:182px;height:182px;border-radius:50%;border:2px solid var(--brand);padding:3px;background:#fff}
.who .portrait div{width:100%;height:100%;border-radius:50%;background:linear-gradient(180deg,#c8d6e6 0%,#e4e9ef 38%,#b9a689 62%,#6c7c88 100%)}
.who .copy-block{position:absolute;left:218px;top:96px;width:224px;font-size:6.2px;line-height:10.4px;color:#8a929b}
.who .copy-block p{margin-bottom:3.6px}
.who .copy-block b{color:#5b636c}
.who .foot{position:absolute;left:16px;right:16px;bottom:10px;display:flex;justify-content:space-between;align-items:center}
.who .foot .brand-mark{font-size:11px}
.who .foot .copy{font-size:6.2px}

/* cover */
.cover-brand{position:absolute;left:332px;top:118px;color:#fff;font-family:"Montserrat",sans-serif;font-weight:600;font-size:24px;letter-spacing:.5px}
.cover-brand small{display:block;font-size:4px;text-align:right;font-weight:500;margin-top:-2px}
.cover-tag{position:absolute;left:333px;top:158px;color:#fff;font-size:11px;line-height:16px}

/* numbered list */
.item{position:absolute;width:96px}
.item .dot{position:absolute;left:-16px;top:-1px;width:11px;height:11px;border-radius:50%;background:var(--brand);color:#fff;font-size:5px;line-height:11px;text-align:center;font-family:"Montserrat",sans-serif}
.item h4{font-weight:normal;color:var(--brand);font-size:7.2px;margin-bottom:3px}

/* icons row */
.svc{position:absolute;top:110px;width:44px;text-align:center}
.svc .ring{width:32px;height:32px;margin:0 auto;border-radius:50%;background:var(--brand);box-shadow:0 0 0 1.5px #fff,0 0 0 2.5px var(--brand);display:flex;align-items:center;justify-content:center}
.svc span{display:block;font-size:3.2px;line-height:3.8px;color:var(--brand);margin-top:5px;font-family:"Montserrat",sans-serif}

/* table */
.grid{position:absolute;left:12px;top:27px;width:230px;border-collapse:collapse;font-size:3.3px}
.grid th{background:var(--brand-deep);color:#fff;font-weight:normal;text-align:left;padding:3px 2px;border:.5px solid #fff}
.grid td{padding:4.4px 2px;border:.5px solid #fff;color:#6a7480}
.grid tr:nth-child(odd) td{background:#c9d9ec}
.grid tr:nth-child(even) td{background:#e3ecf6}

.bar-track{height:4px;background:#e9edf2;position:relative}
.bar-track i{position:absolute;left:0;top:0;bottom:0;background:var(--brand)}
</style>
</head>
<body>

<!-- Cover -->
<div class="label label--vertical" style="left:-20px;top:188px">01 COVER SLIDE</div>
<section class="slide slide--large" style="left:78px" aria-label="Cover slide">
  <svg width="467" height="350" viewBox="0 0 467 350">
    <defs>
      <linearGradient id="coverPhoto" x1="0" y1="0" x2="1" y2="1">
        <stop offset="0" stop-color="#2b3138"/>
        <stop offset=".5" stop-color="#56606a"/>
        <stop offset="1" stop-color="#3a4048"/>
      </linearGradient>
      <linearGradient id="coverBlue" x1="0" y1="0" x2="1" y2="1">
        <stop offset="0" stop-color="#0b3f8c"/>
        <stop offset=".45" stop-color="#1763b8"/>
        <stop offset="1" stop-color="#0a4a9c"/>
      </linearGradient>
    </defs>
    <rect width="467" height="350" fill="url(#coverPhoto)" role="img" aria-label="Photo of a hand touching a glowing network of business icons"/>
    <path d="M248,0 Q345,170 268,350 L467,350 L467,0 Z" fill="url(#coverBlue)"/>
    <path d="M338,0 L467,0 L467,150 Z" fill="#2c7fd0" opacity=".35"/>
    <path d="M248,0 Q345,170 268,350" fill="none" stroke="#fff" stroke-width="3"/>
  </svg>
  <div class="cover-brand">Vantora<small>Pty Ltd</small></div>
  <div class="cover-tag">Helping Your<br>Business Navigate<br>Transformational<br>Change</div>
</section>

<!-- Who we are -->
<div class="label label--vertical" style="left:610px;top:188px">02 INNER</div>
<section class="slide slide--large who" style="left:671px" aria-label="Who we are slide">
  <div class="title">WHO WE ARE</div>
  <div class="badge">01</div>
  <div class="portrait"><div role="img" aria-label="Photo of a city skyline with a river bridge"></div></div>
  <div class="copy-block">
    <p>At Vantora we offer a different kind of management consulting experience. We value our <b>people</b>, which is why we have the best talent available. We believe in <b>partnering</b> with our clients, enabling them to lead change. We focus on <b>execution</b>, which is why we don't just leave our clients with a list of recommendations.</p>
    <p>Vantora was founded in 2013 by Desmond Hale. His aim? To deliver a different type of management consulting experience, one that focused on its people and partnered with businesses to deliver and sustain change.</p>
    <p>Desmond wanted to challenge the traditional business consulting model by building a team of experienced practitioners who have a mindset of achieving together and who are passionate about what they do. These people are recognised and rewarded as the lifeblood of Vantora and are always willing to go the extra mile to help your organisation navigate change.</p>
  </div>
  <div class="foot"><span class="brand-mark">Vantora</span><span class="copy">©2015 Vantora — Management Consulting — Melbourne</span></div>
</section>

<!-- Row 1 -->
<section class="slide slide--thumb" style="left:62px;top:483px">
  <div class="s-title">TITLE WILL COME HERE</div><div class="s-num">02</div>
  <div class="photo" role="img" aria-label="Photo of hands working over charts on a desk" style="left:0;top:26px;width:252px;height:64px;background:linear-gradient(100deg,#d7dde4,#9fbde0 55%,#e6ecf3)"></div>
  <div class="tiny" style="position:absolute;left:10px;top:96px;width:232px">
    <p class="tiny--lead">Lorem ipsum dolor sit amet, consectetur adipiscing elit. Nulla rhoncus euismod ipsum vel vulputate. Integer faucibus ligula vitae libero maximus rhoncus, aenean pulvinar hendrerit cursus.</p>
    <p style="margin-top:3px">Iaculis mi pellentesque dapibus mi ligula vitae feugiat risus vehicula in. Quisque odio lectus tristique sit velit varius imperdiet ornare massa. Vestibulum ante ipsum primis in faucibus orci luctus et ultrices posuere cubilia. Fusce a lacus et sapien cursus tristique ut aliquet aliquet risus non porttitor. Pellentesque dictum lacus sit tortor fringilla interdum sed malesuada eros quis sodales.</p>
  </div>
  <div class="s-foot"><span class="brand-mark">Vantora</span><span class="copy">©2015 Vantora — Management Consulting — Melbourne</span></div>
</section>
<div class="label label--thumb" style="left:62px;top:679px">03 INNER</div>

<section class="slide slide--thumb" style="left:337px;top:483px">
  <div class="s-title">TITLE WILL COME HERE</div><div class="s-num">03</div>
  <div class="item" style="left:52px;top:44px"><span class="dot">1</span><h4>Pellentesque</h4><p class="tiny">Iaculis mi pellentesque dapibus ligula, vitae feugiat risus vehicula. Quisque odio lectus, tristique sit velit varius, imperdiet ornare massa.</p></div>
  <div class="item" style="left:158px;top:44px"><span class="dot">2</span><h4>Risus vehicula</h4><p class="tiny">Iaculis mi pellentesque dapibus ligula, vitae feugiat risus vehicula. Quisque odio lectus, tristique sit velit varius, imperdiet ornare massa.</p></div>
  <div class="item" style="left:52px;top:110px"><span class="dot">3</span><h4>Tristique</h4><p class="tiny">Iaculis mi pellentesque dapibus ligula, vitae feugiat risus vehicula. Quisque odio lectus, tristique sit velit varius, imperdiet ornare massa.</p></div>
  <div class="item" style="left:158px;top:110px"><span class="dot">4</span><h4>Ornare massa</h4><p class="tiny">Iaculis mi pellentesque dapibus ligula, vitae feugiat risus vehicula. Quisque odio lectus, tristique sit velit varius, imperdiet ornare massa.</p></div>
  <div class="s-foot"><span class="brand-mark">Vantora</span><span class="copy">©2015 Vantora — Management Consulting — Melbourne</span></div>
</section>
<div class="label label--thumb" style="left:337px;top:679px">04 INNER</div>

<section class="slide slide--thumb" style="left:612px;top:483px">
  <div class="s-title">TITLE WILL COME HERE</div><div class="s-num">04</div>
  <div class="tiny" style="position:absolute;left:10px;top:45px;width:110px">
    <p style="color:#4f5760">Lorem ipsum dolor sit amet, consectetur adipiscing elit. Nulla rhoncus euismod ipsum vel vulputate, integer faucibus ligula vitae libero maximus.</p>
    <p style="margin-top:3px">Iaculis mi pellentesque dapibus mi ligula, vitae feugiat risus vehicula in. Quisque odio lectus tristique sit velit varius imperdiet ornare massa vestibulum ante ipsum primis.</p>
    <p style="margin-top:3px">Fusce a lacus et sapien cursus tristique, ut aliquet aliquet risus non porttitor pellentesque dictum lacus.</p>
  </div>
  <div class="tiny" style="position:absolute;left:132px;top:45px;width:110px">
    <p>Lorem ipsum dolor sit amet, consectetur adipiscing elit. Nulla rhoncus euismod ipsum vel vulputate, integer faucibus ligula vitae libero maximus rhoncus aenean.</p>
    <p style="margin-top:3px">Vestibulum ante ipsum primis in faucibus orci luctus et ultrices posuere cubilia curae. Fusce a lacus et sapien cursus tristique ut aliquet risus.</p>
    <p style="margin-top:3px">Pellentesque dictum lacus sit tortor fringilla interdum, sed malesuada eros quis sodales ultrices.</p>
  </div>
  <div class="s-foot"><span class="brand-mark">Vantora</span><span class="copy">©2015 Vantora — Management Consulting — Melbourne</span></div>
</section>
<div class="label label--thumb" style="left:612px;top:679px">05 INNER</div>

<section class="slide slide--thumb" style="left:886px;top:483px" aria-label="Section divider slide">
  <svg width="252" height="189" viewBox="0 0 252 189">
    <defs>
      <linearGradient id="dividerPhoto" x1="0" y1="0" x2="1" y2="1">
        <stop offset="0" stop-color="#dfe6ee"/>
        <stop offset=".55" stop-color="#8c8f92"/>
        <stop offset="1" stop-color="#4d5764"/>
      </linearGradient>
    </defs>
    <rect width="252" height="189" fill="url(#dividerPhoto)" role="img" aria-label="Photo of a businessman pointing at a rising chart"/>
    <polyline points="94,90 136,69 177,42 224,37" fill="none" stroke="#fff" stroke-width="1.3"/>
    <g fill="none" stroke="#fff" stroke-width="1.3">
      <circle cx="94" cy="90" r="4"/><circle cx="136" cy="69" r="4"/><circle cx="177" cy="42" r="4"/><circle cx="224" cy="37" r="4"/>
    </g>
    <circle cx="26" cy="92" r="64" fill="none" stroke="#fff" stroke-width="1.5" opacity=".85"/>
    <circle cx="26" cy="92" r="58" fill="#0a4fa0"/>
    <text x="41" y="94.5" text-anchor="middle" fill="#fff" font-family="Montserrat, sans-serif" font-weight="600" font-size="8.5">SERVICES</text>
  </svg>
</section>
<div class="label label--thumb" style="left:886px;top:679px">06 INNER</div>

<!-- Row 2 -->
<section class="slide slide--thumb" style="left:62px;top:710px">
  <div class="s-title">SERVICES</div><div class="s-num">06</div>
  <div class="photo" role="img" aria-label="Photo of a hand signing a document over charts" style="left:0;top:26px;width:252px;height:64px;background:linear-gradient(110deg,#e9edf2,#b8c7d8 50%,#f1f4f7)"></div>
  <div class="svc" style="left:5px"><div class="ring"><svg width="14" height="12" viewBox="0 0 14 12" fill="#fff"><circle cx="7" cy="2" r="1.8"/><circle cx="2.5" cy="8" r="1.6"/><circle cx="7" cy="8" r="1.6"/><circle cx="11.5" cy="8" r="1.6"/><rect x="6.5" y="3.5" width="1" height="3"/></svg></div><span>PROJECT<br>MANAGEMENT</span></div>
  <div class="svc" style="left:54px"><div class="ring"><svg width="14" height="12" viewBox="0 0 14 12" fill="#fff"><rect x="1" y="1" width="12" height="7" rx="1"/><rect x="4" y="9" width="6" height="1.5"/></svg></div><span>BUSINESS<br>PROCESS</span></div>
  <div class="svc" style="left:104px"><div class="ring"><svg width="14" height="14" viewBox="0 0 14 14" fill="none" stroke="#fff" stroke-width="1.5"><path d="M2,7 A5,5 0 0 1 11,4"/><path d="M12,7 A5,5 0 0 1 3,10"/><path d="M9,2 L11,4 L9,6" /><path d="M5,12 L3,10 L5,8"/></svg></div><span>CHANGE<br>MANAGEMENT</span></div>
  <div class="svc" style="left:152px"><div class="ring"><svg width="14" height="12" viewBox="0 0 14 12" fill="#fff"><rect x="1" y="7" width="2.5" height="4"/><rect x="5" y="4" width="2.5" height="7"/><rect x="9" y="1" width="2.5" height="10"/></svg></div><span>BUSINESS<br>ANALYSIS</span></div>
  <div class="svc" style="left:201px"><div class="ring"><svg width="14" height="14" viewBox="0 0 14 14" fill="#fff"><circle cx="7" cy="7" r="3.5"/><g stroke="#fff" stroke-width="1.6"><line x1="7" y1="1" x2="7" y2="13"/><line x1="1" y1="7" x2="13" y2="7"/><line x1="2.8" y1="2.8" x2="11.2" y2="11.2"/><line x1="11.2" y1="2.8" x2="2.8" y2="11.2"/></g><circle cx="7" cy="7" r="1.4" fill="#0056a2"/></svg></div><span>BUSINESS<br>INTELLIGENCE</span></div>
  <div class="s-foot"><span class="brand-mark">Vantora</span><span class="copy">©2015 Vantora — Management Consulting — Melbourne</span></div>
</section>
<div class="label label--thumb" style="left:62px;top:906px">07 INNER</div>

<section class="slide slide--thumb" style="left:337px;top:710px">
  <div class="s-title">SERVICES</div><div class="s-num">07</div>
  <div class="svc" style="left:104px;top:28px"><div class="ring"><svg width="14" height="12" viewBox="0 0 14 12" fill="#fff"><circle cx="7" cy="2" r="1.8"/><circle cx="2.5" cy="8" r="1.6"/><circle cx="7" cy="8" r="1.6"/><circle cx="11.5" cy="8" r="1.6"/><rect x="6.5" y="3.5" width="1" height="3"/></svg></div><span>PROJECT MANAGEMENT</span></div>
  <div class="tiny" style="position:absolute;left:9px;top:84px;width:110px">
    <p class="tiny--lead">SED VOLUTPAT PURUS LIBERO</p>
    <p style="margin-top:2px">Lorem ipsum dolor sit amet, consectetur adipiscing elit. Nullam lacus nulla, placerat eu semper et, sagittis semper ante. Lorem ipsum dolor sit amet, consectetur adipiscing elit. Integer non felis porttitor, semper quam vitae, tristique urna. Donec ac lectus nisi. Pellentesque auctor urna at metus ullamcorper, at elementum odio tincidunt. Blandit porttitor velit, suspendisse congue vel urna id ultricies. Nullam eget justo ex, mauris pharetra quis.</p>
  </div>
  <div class="photo" role="img" aria-label="Photo of a hand drawing a flowchart on a chalkboard" style="left:126px;top:82px;width:115px;height:80px;background:linear-gradient(135deg,#2f3a33,#55605a 55%,#8d9892)"></div>
  <div class="s-foot"><span class="brand-mark">Vantora</span><span class="copy">©2015 Vantora — Management Consulting — Melbourne</span></div>
</section>
<div class="label label--thumb" style="left:337px;top:906px">08 INNER</div>

<section class="slide slide--thumb" style="left:612px;top:710px">
  <div class="s-title">TABLE CONTENT</div><div class="s-num">08</div>
  <table class="grid">
    <tr><th>Ut risus mauris</th><th>Viverra</th><th>Ullamcorper</th><th>Massacanat</th><th>Tempor lorem</th><th>Consequat</th></tr>
    <tr><td>Pharetra</td><td>16,3655</td><td>386565</td><td>46879</td><td>4546</td><td>998</td></tr>
    <tr><td>Donec</td><td>96,696</td><td>5416546</td><td>3634</td><td>56455</td><td>5665</td></tr>
    <tr><td>Ornare</td><td>98,965</td><td>45464</td><td>8974</td><td>44464</td><td>7878</td></tr>
    <tr><td>Proin</td><td>500</td><td>46546</td><td>4787</td><td>9798</td><td>65656</td></tr>
    <tr><td>Nulla</td><td>6,987</td><td>99946</td><td>6584</td><td>46464</td><td>987878</td></tr>
    <tr><td>Elementum</td><td>3,695</td><td>75646</td><td>98798</td><td>56465</td><td>3134</td></tr>
    <tr><td>Mollicul</td><td>1,500</td><td>5454</td><td>54654</td><td>5646</td><td>4498</td></tr>
  </table>
  <div class="tiny" style="position:absolute;left:14px;top:146px;width:226px">
    <p style="color:#4f5760">PHARETRA NEC PURUS</p>
    <p>Nunc vestibulum, lacus ut facilisis gravida, ligula sapien dictum dolor, sed volutpat purus libero eu leo. Sed cursus accumsan diam, id efficitur erat dictum a. Ut ex magna, sagittis a mollis ac, pharetra nec purus molestie urna.</p>
  </div>
  <div class="s-foot"><span class="brand-mark">Vantora</span><span class="copy">©2015 Vantora — Management Consulting — Melbourne</span></div>
</section>
<div class="label label--thumb" style="left:612px;top:906px">09 INNER</div>

<section class="slide slide--thumb" style="left:886px;top:710px">
  <div class="s-title">COMPARISON</div><div class="s-num">10</div>
  <svg style="position:absolute;left:18px;top:50px" width="230" height="52" viewBox="0 0 230 52">
    <g stroke="#eceff3" stroke-width=".5"><line x1="14" y1="2" x2="200" y2="2"/><line x1="14" y1="11" x2="200" y2="11"/><line x1="14" y1="20" x2="200" y2="20"/><line x1="14" y1="29" x2="200" y2="29"/><line x1="14" y1="38" x2="200" y2="38"/></g>
    <g font-size="2.6" fill="#9aa1a9" font-family="Didact Gothic, sans-serif">
      <text x="4" y="3">100%</text><text x="6" y="12">80%</text><text x="6" y="21">60%</text><text x="6" y="30">40%</text><text x="6" y="39">20%</text>
      <text x="28" y="48">January</text><text x="76" y="48">February</text><text x="123" y="48">March</text><text x="170" y="48">April</text>
      <text x="203" y="20">Lorem ipsum</text><text x="203" y="24">Lorem ipsum</text><text x="203" y="28">Lorem ipsum</text>
    </g>
    <g>
      <rect x="30" y="2" width="18" height="9" fill="#8ec4f4"/><rect x="30" y="11" width="18" height="10" fill="#2c8ae0"/><rect x="30" y="21" width="18" height="21" fill="#0056a2"/>
      <rect x="78" y="2" width="18" height="6" fill="#8ec4f4"/><rect x="78" y="8" width="18" height="15" fill="#2c8ae0"/><rect x="78" y="23" width="18" height="19" fill="#0056a2"/>
      <rect x="125" y="2" width="18" height="10" fill="#8ec4f4"/><rect x="125" y="12" width="18" height="10" fill="#2c8ae0"/><rect x="125" y="22" width="18" height="20" fill="#0056a2"/>
      <rect x="172" y="2" width="18" height="8" fill="#8ec4f4"/><rect x="172" y="10" width="18" height="12" fill="#2c8ae0"/><rect x="172" y="22" width="18" height="20" fill="#0056a2"/>
    </g>
    <rect x="199" y="18" width="2.5" height="2" fill="#0056a2"/><rect x="199" y="22" width="2.5" height="2" fill="#2c8ae0"/><rect x="199" y="26" width="2.5" height="2" fill="#8ec4f4"/>
  </svg>
  <div class="tiny" style="position:absolute;left:17px;top:108px;width:62px"><p class="tiny--lead">LOREM IPSUM 1</p><p>At Vantora our goal is to help our clients understand why business process management is another fundamental component of successful business practices. At Vantora we understand that all organisations are a collection of.</p></div>
  <div class="tiny" style="position:absolute;left:93px;top:108px;width:62px"><p class="tiny--lead">LOREM IPSUM 2</p><p>At Vantora our goal is to help our clients understand why business process management is another fundamental component of successful business practices. At Vantora we understand that all organisations are a collection of.</p></div>
  <div class="tiny" style="position:absolute;left:169px;top:108px;width:62px"><p class="tiny--lead">LOREM IPSUM 3</p><p>At Vantora our goal is to help our clients understand why business process management is another fundamental component of successful business practices. At Vantora we understand that all organisations are a collection of.</p></div>
  <div class="s-foot"><span class="brand-mark">Vantora</span><span class="copy">©2015 Vantora — Management Consulting — Melbourne</span></div>
</section>
<div class="label label--thumb" style="left:886px;top:906px">10 INNER</div>

<!-- Row 3 -->
<section class="slide slide--thumb" style="left:62px;top:942px">
  <div class="s-title">TITLE WILL COME HERE</div><div class="s-num">11</div>
  <div class="tiny" style="position:absolute;left:13px;top:32px;width:228px"><p style="color:#4f5760">OUR GOAL AT VANTORA</p><p>Nunc vestibulum, lacus ut facilisis gravida, ligula sapien dictum dolor, sed volutpat purus libero eu leo. Sed cursus accumsan diam, id efficitur erat dictum a. Ut ex magna, sagittis a mollis ac, pharetra nec purus. Fusce vulputate molestie urna. Praesent placerat ipsum orci, a sodales neque bibendum at. Proin ullamcorper finibus lorem, eu interdum sem porta.</p></div>
  <div style="position:absolute;left:15px;top:64px;width:130px" class="tiny">
    <div style="display:flex;align-items:center;margin-bottom:5px"><span class="tiny--lead" style="width:46px">Ut risus mauris</span><div class="bar-track" style="flex:1"><i style="width:50%"></i></div></div>
    <div style="display:flex;align-items:center;margin-bottom:5px"><span class="tiny--lead" style="width:46px">Viverra sit amet</span><div class="bar-track" style="flex:1"><i style="width:62%;background:#2c8ae0"></i></div></div>
    <div style="display:flex;align-items:center;margin-bottom:5px"><span class="tiny--lead" style="width:46px">Ullamcorper sed</span><div class="bar-track" style="flex:1"><i style="width:30%;background:#6fb3ee"></i></div></div>
    <div style="display:flex;align-items:center"><span class="tiny--lead" style="width:46px">Morbi vitae lectus</span><div class="bar-track" style="flex:1"><i style="width:10%;background:#a9d2f6"></i></div></div>
  </div>
  <div class="photo" role="img" aria-label="Photo of two business people shaking hands at a sunset window" style="left:150px;top:62px;width:91px;height:45px;background:linear-gradient(180deg,#f0a24a,#b9622a 55%,#3a2a22)"></div>
  <div class="tiny" style="position:absolute;left:15px;top:125px;width:50px"><p class="tiny--lead">UT RISUS MAURIS</p><p>At Vantora our goal is to help our clients understand why business process management is another.</p></div>
  <div class="tiny" style="position:absolute;left:73px;top:125px;width:50px"><p class="tiny--lead">UT RISUS MAURIS</p><p>At Vantora our goal is to help our clients understand why business process management is another.</p></div>
  <div class="tiny" style="position:absolute;left:131px;top:125px;width:50px"><p class="tiny--lead">UT RISUS MAURIS</p><p>At Vantora our goal is to help our clients understand why business process management is another.</p></div>
  <div class="tiny" style="position:absolute;left:189px;top:125px;width:50px"><p class="tiny--lead">UT RISUS MAURIS</p><p>At Vantora our goal is to help our clients understand why business process management is another.</p></div>
  <div class="s-foot"><span class="brand-mark">Vantora</span><span class="copy">©2015 Vantora — Management Consulting — Melbourne</span></div>
</section>
<div class="label label--thumb" style="left:62px;top:1137px">11 INNER</div>

<section class="slide slide--thumb" style="left:337px;top:942px">
  <div class="photo" role="img" aria-label="Photo of a businessman in a dark suit and tie" style="left:0;top:0;width:98px;height:174px;background:linear-gradient(90deg,#f2f2f2,#3a3d42 40%,#1f2226 70%,#e9e9e9)"></div>
  <div class="s-title" style="left:98px">TITLE</div><div class="s-num">12</div>
  <div class="tiny" style="position:absolute;left:112px;top:38px;width:128px">
    <p style="color:#4f5760">Lorem ipsum dolor sit amet, consectetur adipiscing elit. Nulla rhoncus euismod ipsum vel vulputate. Integer faucibus ligula vitae libero maximus rhoncus, aenean pulvinar hendrerit cursus.</p>
    <p style="margin-top:4px">Iaculis mi pellentesque dapibus mi ligula, vitae feugiat risus vehicula in. Quisque odio lectus tristique sit velit varius imperdiet ornare massa. Vestibulum ante ipsum primis in faucibus orci.</p>
    <p style="margin-top:4px">Fusce a lacus et sapien cursus tristique, ut aliquet aliquet risus non porttitor. Pellentesque dictum lacus sit tortor fringilla interdum, sed malesuada eros quis sodales ultrices.</p>
  </div>
  <div class="s-foot"><span class="brand-mark">Vantora</span><span class="copy">©2015 Vantora — Management Consulting — Melbourne</span></div>
</section>
<div class="label label--thumb" style="left:337px;top:1137px">12 INNER</div>

<section class="slide slide--thumb" style="left:612px;top:942px">
  <div class="s-title">BLANK SLIDE</div><div class="s-num">13</div>
  <div class="s-foot"><span class="brand-mark">Vantora</span><span class="copy">©2015 Vantora — Management Consulting — Melbourne</span></div>
</section>
<div class="label label--thumb" style="left:612px;top:1137px">13 INNER</div>

<section class="slide slide--thumb" style="left:886px;top:942px" aria-label="Closing slide">
  <svg width="252" height="189" viewBox="0 0 252 189">
    <defs>
      <linearGradient id="closingPhoto" x1="0" y1="0" x2="1" y2="1">
        <stop offset="0" stop-color="#9a5a2c"/>
        <stop offset=".5" stop-color="#c98a4a"/>
        <stop offset="1" stop-color="#4a2c1c"/>
      </linearGradient>
    </defs>
    <rect width="252" height="189" fill="url(#closingPhoto)" role="img" aria-label="Photo of a steaming blue mug by a rain covered window"/>
    <circle cx="126" cy="2" r="56" fill="#fff"/>
    <text x="126" y="30" text-anchor="middle" fill="#0056a2" font-family="Montserrat, sans-serif" font-weight="600" font-size="11">THANK YOU !</text>
  </svg>
</section>
<div class="label label--thumb" style="left:886px;top:1137px">14 INNER</div>

</body>
</html>
```